Velm Biologics product brochure - credibility, sophistication, cutting-edge

Velm Biologics, Inc. is a company that provides the most cutting-edge regenerative medicine products in the US. This brochure will highlight our stem cell products VelmBase and VelmArc, educating the public/patients and physician alike on what stem cells are, comparison of various stem cell treatments available, and what makes Velm products different. This serves as a marketing tool to reach both patients and physicians.

I have included the current brochure, which I am not completely happy with. I want a brochure that portrays that we are a top-notch company, with credibility and sophistication. I will make slight content change, but most contents will stay.

Please refer to current website for further information: www.velmbiologics-example.com

Low design quality

Target Market(s)

doctors and patients.

Industry/Entity Type

Healthcare

Font styles to use
Serif
Other font styles liked:
• anything that looks best on brochures & easy to read

Colors

Designer to choose colors to be used in the design.

Requirements
Must have
• Clean & modern feel, eye-catching.
• Would prefer bi-fold rather than tri-fold, because I think it looks fresher.
• Easy to read, clear.
• beautiful, elegant, stunning
Should not have
• Please DO NOT recycle graphics or images from the old brochure. I would like this for sure to be brand new, fresh and original.

```html
<!DOCTYPE html>
<html lang="en">
<head>
<meta charset="utf-8">
<title>Stem Cell Sources and Pros &amp; Cons — Velm Biologics</title>
<link href="https://fonts.googleapis.com/css2?family=Aldrich&family=Lato:wght@400;700&display=swap" rel="stylesheet">
<style>
  :root {
    --ink-dark: #1d1d1f;
    --gold: #c9962f;
    --gold-light: #ecd9a8;
    --row-grey: #dfe0e2;
    --text: #3a3a3c;
    --page: #f3f4f6;
    --white: #ffffff;
    --mol-blue: #4f7d9c;
    --mol-light: #cfe3ef;
  }
  * { box-sizing: border-box; margin: 0; padding: 0; }
  html, body { width: 1034px; height: 1200px; overflow: hidden; background: var(--page); }
  .sheet {
    position: relative; width: 1034px; height: 1200px; overflow: hidden;
    background: linear-gradient(180deg, var(--white) 0%, var(--page) 100%);
    font-family: "Lato", sans-serif; color: var(--text);
  }
  .sheet-header {
    position: absolute; left: 0; top: 0; width: 1034px; height: 145px;
    background: var(--ink-dark);
  }
  .sheet-title {
    position: absolute; left: 0; top: 58px; width: 100%; text-align: center;
    font-family: "Aldrich", sans-serif; font-size: 48px; color: var(--white);
    letter-spacing: 1px;
  }
  .accent-sweep { position: absolute; left: 0; top: 0; width: 1034px; height: 800px; }
  .compare-panel {
    position: absolute; left: 20px; top: 150px; width: 976px; height: 620px;
    background: rgba(255,255,255,0.9); border-radius: 12px;
  }
  .compare-table {
    position: absolute; left: 49px; top: 196px; width: 917px;
    border-collapse: collapse; font-size: 15.5px; line-height: 18px;
  }
  .compare-table th {
    font-family: "Aldrich", sans-serif; font-weight: 400; font-size: 19px;
    color: var(--ink-dark); text-align: left; vertical-align: bottom;
    height: 54px; padding-bottom: 10px;
  }
  .compare-table td { height: 71px; vertical-align: middle; padding-right: 10px; }
  .compare-table tbody tr:nth-child(odd) { background: var(--row-grey); }
  .compare-table .row-label { padding-left: 44px; width: 211px; font-weight: 400; }
  .compare-table td.cell { font-weight: 700; color: #4a4a4c; }
  .col-cord { width: 222px; }
  .col-amnio { width: 221px; }
  .molecule-art {
    position: absolute; left: 0; top: 790px; width: 560px; height: 410px;
    background: radial-gradient(ellipse at 30% 60%, var(--mol-blue) 0%, var(--mol-light) 45%, rgba(243,244,246,0) 75%);
  }
  .legal-note {
    position: absolute; right: 68px; top: 912px; width: 560px;
    text-align: right; font-size: 17.5px; line-height: 21.8px; color: var(--text);
  }
</style>
</head>
<body>
<main class="sheet">
  <svg class="accent-sweep" viewBox="0 0 1034 800" aria-hidden="true">
    <defs>
      <linearGradient id="goldBand" x1="0" y1="0" x2="1" y2="1">
        <stop offset="0" stop-color="#a87520"/>
        <stop offset="0.5" stop-color="#e0b860"/>
        <stop offset="1" stop-color="#b6832a"/>
      </linearGradient>
      <linearGradient id="goldWash" x1="0" y1="0" x2="1" y2="0">
        <stop offset="0" stop-color="#ffffff" stop-opacity="0"/>
        <stop offset="1" stop-color="#ecd9a8" stop-opacity="0.8"/>
      </linearGradient>
    </defs>
    <polygon points="0,130 1034,165 1034,700 1010,700 1010,175 0,150" fill="url(#goldBand)"/>
    <polygon points="300,160 1034,200 1034,660 980,600 980,240" fill="url(#goldWash)"/>
    <polygon points="0,0 1034,0 1034,210 0,135" fill="var(--ink-dark)"/>
  </svg>
  <header class="sheet-header">
    <h1 class="sheet-title">Stem Cell Sources and Pros &amp; Cons</h1>
  </header>
  <div class="compare-panel"></div>

  <table class="compare-table">
    <thead>
      <tr>
        <th></th>
        <th class="col-cord">Umbilical Cord</th>
        <th class="col-amnio">&nbsp;Amniotic</th>
        <th>Autologous<br>(Adipose Vs. Bone Marrow)</th>
      </tr>
    </thead>
    <tbody>
      <tr><td class="row-label">Stem Cell Type</td><td class="cell">MSC &amp; HSC</td><td class="cell">MSC &amp; Epithelial derived (no CD34 cells)</td><td class="cell">MSC Vs. MSC &amp; HSC</td></tr>
      <tr><td class="row-label">Concentration</td><td class="cell">Customizable for precise individual applications (10 million/cc VelmArc, 30 million/cc VelmBase)</td><td class="cell">Few live stem cells</td><td class="cell">1 to 30 million/cc (dependent on patient age, health, equipment and operator skills)</td></tr>
      <tr><td class="row-label">Quality of Cells</td><td class="cell">Young / robust / contains unique healing factors</td><td class="cell">Young / larger proportion of cellular debris /approved wound healing product</td><td class="cell">Patient-dependent upon age and health (cell quality declines from advancing age &amp; disease state)</td></tr>
      <tr><td class="row-label">Adverse<br>Reaction</td><td class="cell">Minimal</td><td class="cell">Minimal</td><td class="cell">Pain, risk of infection, and other risks associated with surgical procedures</td></tr>
      <tr><td class="row-label">Consistency of<br>Results</td><td class="cell">Consistent (based on quality of cells, concentration, growth factors &amp; matrix)</td><td class="cell">Consistent (based on concentration, growth factors &amp; matrix)</td><td class="cell">Variable (operator-dependent, patient age and healthdependent)</td></tr>
      <tr><td class="row-label">Ease of Use</td><td class="cell">Thaw and infuse / inject</td><td class="cell">Thaw and infuse / inject</td><td class="cell">Surgical procedure<br>and processing</td></tr>
      <tr><td class="row-label">Time In Office</td><td class="cell">60 minutes</td><td class="cell">60 minutes</td><td class="cell">3-5 hours</td></tr>
    </tbody>
  </table>

  <div class="molecule-art" role="img" aria-label="Illustration of glossy blue molecular spheres joined by bonds"></div>

  <p class="legal-note">Note: Velm’s representations concerning FDA compliance relate strictly to the sourcing of stem cells and not to the FDA approval status, safety risks, or effectiveness of particular treatments. Patients are encouraged to discuss with their physicians any questions about the particular use of stem cells in treatments which may be investigational and/or unapproved. In addition, Velm makes no representation concerning the limitations imposed by state or foreign regulations of stem cell treatment, and all representations by Velm are void in jurisdictions that prohibit the use of stem cells.</p>
</main>
</body>
</html>
```